Business Card Design

I am selling Cruelty Free/not tested on animal products.
Ideally I would like pictures of rabbits/guinea pigs/Beagle(dog)/rat/mice, as these are the main creatures that are tested on.
Background of card Earth, clouds or rainbow.
Yes I am an animal activist.
My favorite colours are purple and green.

Industry/Entity Type

Business

Contact Information for Business Card

GENTLY FROM MEADOW
Cruelty Free Products
Maren Holtby
0483 529 714

```html
<!DOCTYPE html>
<html lang="en">
<head>
<meta charset="utf-8">
<title>Gently From Meadow – Business Card</title>
<link rel="stylesheet" href="https://fonts.googleapis.com/css2?family=Cinzel:wght@400;500&display=swap">
<style>
  :root {
    --stage: #d9d9db;
    --card-purple: #7150a6;
    --cloud-pink: #e8207f;
    --cloud-violet: #7a4fc0;
    --cloud-yellow: #d9e432;
    --cloud-orange: #f2841f;
    --cloud-red: #ea2a1e;
    --cloud-green: #55b84a;
    --panel: #ffffff;
    --ink: #111111;
    --green: #1f8a3a;
    --guinea-fur: #b98a5e;
    --beagle-fur: #8a6240;
  }
  * { box-sizing: border-box; margin: 0; padding: 0; }
  html, body {
    width: 1200px; height: 1000px; overflow: hidden;
    background: var(--stage);
  }
  .card {
    position: absolute; left: 150px; top: 230px;
    width: 900px; height: 540px;
    border-radius: 26px; overflow: hidden;
    background: var(--card-purple);
    box-shadow: 0 10px 30px rgba(0,0,0,0.25);
  }
  .card__clouds {
    position: absolute; inset: 0 0 90px 0;
    background: linear-gradient(100deg,
      var(--cloud-pink) 0%, var(--cloud-violet) 30%, var(--cloud-green) 52%,
      var(--cloud-yellow) 70%, var(--cloud-orange) 85%, var(--cloud-red) 100%);
  }
  .card__clouds::after {
    content: ""; position: absolute; inset: 0;
    background: linear-gradient(180deg, rgba(113,80,166,0) 60%, var(--card-purple) 100%);
  }
  .panel {
    position: absolute; left: 80px; top: 75px;
    width: 760px; height: 390px;
    background: var(--panel);
    box-shadow: 0 4px 10px rgba(0,0,0,0.25);
    text-align: center;
  }
  .panel__clouds {
    position: absolute; left: 0; right: 0; top: 0; height: 180px;
    background: linear-gradient(90deg,
      rgba(232,32,127,0.35), rgba(122,79,192,0.45) 30%, rgba(85,184,74,0.35) 55%,
      rgba(217,228,50,0.45) 75%, rgba(234,42,30,0.5));
    -webkit-mask-image: linear-gradient(180deg, #000 20%, transparent 100%);
            mask-image: linear-gradient(180deg, #000 20%, transparent 100%);
  }
  .brand {
    position: relative; margin-top: 92px;
    font-family: "Cinzel", serif; font-weight: 400;
    font-size: 54px; letter-spacing: 1px; color: var(--ink);
    line-height: 1; white-space: nowrap;
  }
  .tagline {
    position: relative; display: inline-block; margin-top: 14px;
    font-family: "Cinzel", serif; font-size: 32px; color: var(--green);
    padding-bottom: 2px; border-bottom: 2px solid var(--green);
    line-height: 1.1;
  }
  .contact {
    position: relative; margin-top: 36px; padding-right: 60px;
    font-family: "Cinzel", serif; color: var(--green);
  }
  .contact__name { font-size: 44px; line-height: 1.1; font-weight: 500; white-space: nowrap; }
  .contact__phone { font-size: 40px; line-height: 1.1; white-space: nowrap; }
  .animal { position: absolute; border-radius: 40% 40% 30% 30%; }
  .animal--guinea-pig {
    left: 18px; top: 340px; width: 180px; height: 160px;
    background: radial-gradient(circle at 45% 45%, #f3ece3 0%, var(--guinea-fur) 70%);
  }
  .animal--beagle {
    left: 650px; top: 285px; width: 230px; height: 235px;
    background: linear-gradient(160deg, #3a2e26 0%, var(--beagle-fur) 40%, #f1ede8 80%);
  }
</style>
</head>
<body>
  <div class="card">
    <div class="card__clouds" role="img" aria-label="Colourful rainbow cloud pattern background"></div>
    <div class="panel">
      <div class="panel__clouds" role="img" aria-label="Soft rainbow clouds fading into white"></div>
      <h1 class="brand">GENTLY FROM MEADOW</h1>
      <p class="tagline">Cruelty Free Products</p>
      <div class="contact">
        <p class="contact__name">Maren Holtby</p>
        <p class="contact__phone">0483 529 714</p>
      </div>
    </div>
    <div class="animal animal--guinea-pig" role="img" aria-label="Photo of a brown and white guinea pig"></div>
    <div class="animal animal--beagle" role="img" aria-label="Photo of a beagle dog lying down"></div>
  </div>
</body>
</html>
```